Sandwich Board and Poster design promoting a medical aesthetic clinic

I am looking for a clean, modern and relaxing design promoting a medical physician-led aesthetic clinic.
Services offered are neuromodulator treatment (Quelvo) and Dermal Fillers.
Logo must be included.
Use the tag line "Refresh your look, revive your spirit."
Address is 204-205 27361 92 Ave, Surrey, V7K 2M4
604-555-0148
email - info@lumawellpine.ca
www.lumawellpine.ca

```html
<!DOCTYPE html>
<html lang="en">
<head>
<meta charset="utf-8">
<title>Lumawell Pine – Refresh your look, revive your spirit</title>
<link href="https://fonts.googleapis.com/css2?family=Playfair+Display:wght@500;600&family=Poppins:wght@400;500;600;700&display=swap" rel="stylesheet">
<style>
  :root {
    --navy: #17294a;
    --ink: #0d1424;
    --ink-soft: #1a2236;
    --gold: #dbb42c;
    --gold-deep: #9c7d1c;
    --white: #ffffff;
    --cream: #f7f5f2;
    --skin: #efd3c4;
    --petal: #e2b84a;
  }
  * { margin: 0; padding: 0; box-sizing: border-box; }
  html, body { width: 783px; height: 1200px; overflow: hidden; background: var(--cream); }
  .poster { position: relative; width: 783px; height: 1200px; overflow: hidden; font-family: "Poppins", sans-serif; }

  .hero { position: absolute; left: 0; top: 0; width: 783px; height: 662px;
    background: linear-gradient(160deg, #fbfaf8 0%, #f2efea 60%, #f8f6f2 100%); }
  .hero-photo { position: absolute; left: 0; top: 0; width: 410px; height: 662px;
    background: radial-gradient(ellipse at 55% 40%, var(--skin) 0%, #f3e2d8 45%, rgba(248,246,242,0) 75%),
                radial-gradient(ellipse at 25% 90%, var(--petal) 0%, rgba(226,184,74,0) 45%); }

  .headline { position: absolute; font-family: "Playfair Display", serif; font-weight: 500; line-height: 1; white-space: nowrap; }
  .headline.navy { color: var(--navy); font-size: 76px; letter-spacing: -1px; }
  .headline.gold { color: var(--gold); font-size: 104px; letter-spacing: -2px; }

  .lower { position: absolute; left: 0; top: 662px; width: 783px; height: 538px;
    background: linear-gradient(150deg, var(--ink-soft) 0%, var(--ink) 55%, #151c2e 100%); }

  .pill { position: absolute; display: flex; align-items: center; justify-content: center; gap: 8px;
    border-radius: 24px; font-weight: 600; font-size: 17px; white-space: nowrap; }
  .pill svg { width: 18px; height: 18px; }
  .pill.dark { left: 150px; top: 646px; width: 482px; height: 40px; background: var(--navy);
    border: 2px solid var(--gold); color: var(--white); }
  .pill.gold { left: 165px; top: 962px; width: 453px; height: 39px; background: var(--gold); color: var(--navy); }

  .services-title { position: absolute; left: 0; top: 728px; width: 783px; text-align: center;
    color: var(--gold); font-size: 24px; letter-spacing: 4px; font-weight: 400; }
  .services-side { position: absolute; left: 108px; top: 808px; color: var(--gold);
    font-size: 37px; font-weight: 500; line-height: 41px; }
  .service-icon { position: absolute; left: 321px; width: 58px; height: 58px; border: 1.5px solid var(--gold); border-radius: 50%;
    background: radial-gradient(circle at 50% 45%, var(--gold-deep) 0%, rgba(156,125,28,0.35) 55%, rgba(13,20,36,0) 80%); }
  .service-icon.one { top: 796px; }
  .service-icon.two { top: 859px; }
  .service-name { position: absolute; left: 393px; color: var(--white); font-weight: 600; font-size: 26px; line-height: 30px; white-space: nowrap; }
  .service-name.one { top: 800px; }
  .service-name.two { top: 876px; }

  .brand { position: absolute; left: 148px; top: 1098px; width: 200px; text-align: center;
    color: var(--white); font-size: 18px; font-weight: 400; letter-spacing: 3px; white-space: nowrap; }

  .contact { position: absolute; left: 364px; display: flex; align-items: center; gap: 8px; color: var(--white); white-space: nowrap; }
  .contact svg { width: 16px; height: 16px; flex: none; }
  .contact.phone { top: 1048px; font-size: 29px; font-weight: 600; }
  .contact.email { top: 1085px; font-size: 19px; }
  .contact.web { top: 1110px; font-size: 19px; }
</style>
</head>
<body>
<main class="poster">
  <section class="hero">
    <div class="hero-photo" role="img" aria-label="Photo of a woman receiving a facial injection, framed by golden flowers"></div>
    <h1>
      <span class="headline navy" style="left:405px;top:100px;">Refresh</span>
      <span class="headline navy" style="left:405px;top:160px;">your</span>
      <span class="headline gold" style="left:403px;top:225px;">LOOK</span>
      <span class="headline navy" style="left:403px;top:337px;">Revive</span>
      <span class="headline navy" style="left:403px;top:397px;">your</span>
      <span class="headline gold" style="left:397px;top:463px;">SPIRIT</span>
    </h1>
  </section>

  <section class="lower" role="img" aria-label="Dark navy marble texture with gold veins"></section>

  <div class="pill dark">
    <svg viewBox="0 0 24 24" fill="none" stroke="#dbb42c" stroke-width="2"><path d="M12 21s-6-6.2-6-11a6 6 0 0 1 12 0c0 4.8-6 11-6 11z"/><circle cx="12" cy="10" r="2.2"/></svg>
    204-205 27361 92 Ave, Surrey, V7K 2M4
  </div>

  <h2 class="services-title">SERVICES WE OFFER</h2>
  <p class="services-side">SERVICES<br>WE OFFER</p>

  <div class="service-icon one" role="img" aria-label="Line icon of a face receiving an injection"></div>
  <div class="service-icon two" role="img" aria-label="Line icon of lips receiving a filler injection"></div>
  <p class="service-name one">Neuromodulator<br>treatment (Quelvo)</p>
  <p class="service-name two">Dermal Fillers</p>

  <div class="pill gold">
    <svg viewBox="0 0 24 24" fill="none" stroke="#17294a" stroke-width="2"><path d="M12 21s-6-6.2-6-11a6 6 0 0 1 12 0c0 4.8-6 11-6 11z"/><circle cx="12" cy="10" r="2.2"/></svg>
    204-205 27361 92 Ave, Surrey, V7K 2M4
  </div>

  <p class="brand">LUMAWELL PINE</p>

  <p class="contact phone">
    <svg viewBox="0 0 24 24" fill="#dbb42c"><path d="M6.6 10.8a15 15 0 0 0 6.6 6.6l2.2-2.2a1 1 0 0 1 1-.25 11.4 11.4 0 0 0 3.6.57 1 1 0 0 1 1 1V20a1 1 0 0 1-1 1A17 17 0 0 1 3 4a1 1 0 0 1 1-1h3.5a1 1 0 0 1 1 1c0 1.250.2 2.450.57 3.57a1 1 0 0 1-.25 1z"/></svg>
    604-555-0148
  </p>
  <p class="contact email">
    <svg viewBox="0 0 24 24" fill="none" stroke="#dbb42c" stroke-width="2"><rect x="3" y="6" width="18" height="13" rx="1"/><path d="M3 7l9 6 9-6"/></svg>
    info@lumawellpine.ca
  </p>
  <p class="contact web">
    <svg viewBox="0 0 24 24" fill="none" stroke="#dbb42c" stroke-width="2"><circle cx="12" cy="12" r="9"/><path d="M3 12h18M12 3c3 3.5 3 14.5 0 18M12 3c-3 3.5-3 14.5 0 18"/></svg>
    www.lumawellpine.ca
  </p>
</main>
</body>
</html>
```